Team 5164 Reunion and Anniversary Party!

My work team will be having a reunion party for past and present members which will also serve as a 25th company anniversary celebration for two of our leaders. We were hoping to secure a fun (yet classy) design that could be used in an email template for a mass email invitation. Thank you!

```html
<!DOCTYPE html>
<html lang="en">
<head>
<meta charset="utf-8">
<title>Team 5164 Reunion &amp; Anniversary Party</title>
<link rel="stylesheet" href="https://fonts.googleapis.com/css2?family=DM+Serif+Display&family=Source+Sans+3:wght@400;500;600&display=swap">
<style>
  :root {
    --page-bg: #ffffff;
    --card-top: #1d2831;
    --card-bottom: #0f161c;
    --gold-light: #f6d27a;
    --gold-mid: #d9a441;
    --gold-deep: #a8742c;
    --gold-line: #c89a4a;
    --leaf-tone: rgba(120, 128, 132, 0.28);
    --leaf-edge: rgba(214, 170, 86, 0.22);
  }
  * { box-sizing: border-box; margin: 0; padding: 0; }
  html, body {
    width: 1200px;
    height: 1000px;
    overflow: hidden;
    background: var(--page-bg);
  }
  .canvas { position: relative; width: 1200px; height: 1000px; }

  .invitation {
    position: absolute;
    left: 303px;
    top: 79px;
    width: 595px;
    height: 842px;
    background: radial-gradient(ellipse at 50% 45%, var(--card-top) 0%, var(--card-bottom) 100%);
    overflow: hidden;
  }
  .frame-lines { position: absolute; inset: 0; }

  .ornament {
    position: absolute;
    background: radial-gradient(ellipse at center, var(--leaf-tone) 0%, var(--leaf-edge) 45%, rgba(0,0,0,0) 72%);
  }
  .ornament--corner-top { left: -20px; top: 10px; width: 210px; height: 240px; }
  .ornament--corner-bottom { right: -20px; bottom: 10px; width: 210px; height: 240px; }
  .ornament--wreath-top { left: 145px; top: 165px; width: 290px; height: 110px; }
  .ornament--wreath-bottom { left: 175px; top: 425px; width: 290px; height: 115px; }

  .gold-text {
    background: linear-gradient(180deg, var(--gold-light) 0%, var(--gold-mid) 55%, var(--gold-deep) 100%);
    -webkit-background-clip: text;
    background-clip: text;
    color: transparent;
  }
  .eyebrow {
    position: absolute;
    left: 0; right: 0;
    text-align: center;
    font-family: "Source Sans 3", sans-serif;
    font-weight: 500;
    font-size: 13px;
    letter-spacing: 3px;
    color: var(--gold-mid);
  }
  .eyebrow--intro { top: 116px; }
  .eyebrow--celebration { top: 550px; }

  .milestone {
    position: absolute;
    left: 0; right: 0;
    top: 270px;
    text-align: center;
    font-family: "DM Serif Display", serif;
    line-height: 1;
  }
  .milestone__number { font-size: 150px; letter-spacing: -4px; }
  .milestone__suffix {
    position: absolute;
    top: 20px;
    left: 369px;
    font-size: 30px;
  }

  .event-title {
    position: absolute;
    left: 0; right: 0;
    top: 584px;
    text-align: center;
    font-family: "DM Serif Display", serif;
    font-weight: 400;
    font-size: 40px;
    line-height: 44px;
  }
  .event-details {
    position: absolute;
    left: 0; right: 0;
    text-align: center;
    font-family: "Source Sans 3", sans-serif;
    font-size: 14px;
    color: var(--gold-mid);
  }
  .event-details--when { top: 702px; }
  .event-details--when .divider { margin: 0 6px; color: var(--gold-light); }
  .event-details--where { top: 731px; }
</style>
</head>
<body>
<div class="canvas">
  <section class="invitation">
    <svg class="frame-lines" width="595" height="842" viewBox="0 0 595 842" aria-hidden="true">
      <g fill="none" stroke="var(--gold-line)" stroke-width="1.2">
        <!-- outer frame -->
        <path d="M212 31 H559 V619"/>
        <circle cx="207" cy="42" r="5"/>
        <circle cx="564" cy="27" r="4"/>
        <circle cx="552" cy="625" r="5"/>
        <path d="M35 218 V809 H382"/>
        <circle cx="44" cy="215" r="5"/>
        <circle cx="30" cy="813" r="4"/>
        <circle cx="387" cy="801" r="5"/>
        <!-- octagon around milestone -->
        <path d="M152 275 V425"/>
        <path d="M442 278 V432"/>
        <path d="M152 275 L200 240"/>
        <path d="M442 278 L395 242"/>
        <path d="M152 425 L190 455"/>
        <path d="M442 432 L405 462"/>
        <circle cx="148" cy="268" r="3"/>
        <circle cx="432" cy="266" r="2.5"/>
        <circle cx="438" cy="271" r="2.5"/>
        <circle cx="444" cy="276" r="2.5"/>
        <circle cx="155" cy="425" r="2.5"/>
        <circle cx="160" cy="431" r="2.5"/>
        <circle cx="166" cy="436" r="2.5"/>
        <circle cx="447" cy="432" r="3"/>
      </g>
    </svg>

    <div class="ornament ornament--corner-top" role="img" aria-label="Gold leaf and berry spray ornament in the top left corner"></div>
    <div class="ornament ornament--corner-bottom" role="img" aria-label="Gold leaf and berry spray ornament in the bottom right corner"></div>
    <div class="ornament ornament--wreath-top" role="img" aria-label="Gold leafy branch above the anniversary number"></div>
    <div class="ornament ornament--wreath-bottom" role="img" aria-label="Gold leafy branch below the anniversary number"></div>

    <p class="eyebrow eyebrow--intro">JOIN US FOR THE</p>

    <div class="milestone">
      <span class="milestone__number gold-text">25</span><span class="milestone__suffix gold-text">TH</span>
    </div>

    <p class="eyebrow eyebrow--celebration">CELEBRATION OF</p>

    <h1 class="event-title gold-text">Team 5164 Reunion &amp;<br>Anniversary Party!</h1>

    <p class="event-details event-details--when">May 28th<span class="divider">|</span>4 o'clock</p>
    <p class="event-details event-details--where">Address: Lorem Country Ride 15 - Ipsum - MO, 65466</p>
  </section>
</div>
</body>
</html>
```